Packaging label for Multi purpose ointment/balm

I would like to change packaging label (design) for multi purpose ointment (balm) that I have. Name of company is Vira Lunos and I named the product (ointment) TENDREX. I attached pictures of existing label that i have (first file). The other 3 files are just changes that I was thinking to add. I would like to completely change look (design) of label. I was thinking to remove name TENDREX and make it more stand out "multi purpose ointment" instead. But word TENDREX can also stay on it if you think that would come out better. I was also thinking to change it to balm instead of ointment.
So I would like on label to stand out:
-multi purpose ointment or balm
-skin
-muscles
-joints
Ointment would be mostly use for skin problems, so I was thinking to add something like: cuts, burns, scrapes,... next to the word "skin".
Please feel free to use creation and completely change the look of label (design), because I want completely different design, and not similar design.
Here is description of multi purpose ointment:
Tendrex is multi purpose ointment with pain relief, anti-inflammatory and other healing properties for skin, muscles and joints. It is all natural, non-gmo, and made from the finest plant-based ingredients.
PURPOSE AND USE
Tendrex is a multi purpose ointment suitable for everyday use. It can be used to treat various injuries and phenomena of the skin such as wounds, sores, ulcers, mastitis, insect bites, burns, whitlow, herpes, aphthae, bruises, blisters and fungal infections with healing effects generally visible within 3 days. Do not apply directly on open wounds. It may be covered with a loosely wrapped sterile bandage that does not inhibit blood circulation. Tendrex also reduces swelling and relieves pain caused by rheumatism, gout, sciatica, arthritis. It can also be applied as a massage balm to improve blood circulation, reduce inflammation of muscles and ligaments, and alleviate back pain, joint pain, shoulder pain and other muscle soreness. For best results, massage affected area several times a day. In addition, the ointment can be used to effectively relieve nasal and upper respiratory congestion (apply around the nose, chest and throat). Tendrex may also be applied as a daily moisturizer to revitalize skin and prevent the formation of stretch marks. After use, the skin is soft and toned.
pellot Market(s)
Stores like fresh orchard, bazmart, pellot, vandro, stores with natural products,...
Industry/Entity Type
It Company
Font styles to use
Requirements
Nice to have
- I want completely different design. Not similar design.

```html
<!DOCTYPE html>
<html lang="en">
<head>
<meta charset="utf-8">
<title>Vira Lunos – Multi Purpose Ointment Label</title>
<link href="https://fonts.googleapis.com/css2?family=Oswald:wght@700&family=Montserrat:wght@600;700&display=swap" rel="stylesheet">
<style>
  :root{
    --page:#f4f4f4;
    --green-deep:#0f4f1c;
    --green-mid:#2f8f2a;
    --green-bright:#6cc43a;
    --green-mint:#8fe0c8;
    --gold-light:#ffe58a;
    --gold:#f7b733;
    --orange:#e8741a;
    --ring-green:#0e6a1e;
    --red:#c0161e;
    --white:#ffffff;
    --pill:#123d17;
  }
  html,body{margin:0;padding:0;width:1200px;height:1200px;overflow:hidden;background:var(--page);}
  .canvas{width:1200px;height:1200px;display:flex;align-items:center;justify-content:center;}
  .label{width:1100px;height:740px;display:block;box-shadow:0 12px 30px rgba(0,0,0,.18);}
  .headline{font-family:'Oswald',sans-serif;font-weight:700;fill:var(--green-deep);}
  .brand-name{font-family:'Montserrat',sans-serif;font-weight:700;fill:var(--white);font-size:32px;}
  .use-area{font-family:'Montserrat',sans-serif;font-weight:600;fill:var(--white);font-size:42px;}
  .size{font-family:'Montserrat',sans-serif;font-weight:600;fill:var(--white);font-size:24px;}
</style>
</head>
<body>
<main class="canvas">
  <svg class="label" viewBox="0 0 1040 700" xmlns="http://www.w3.org/2000/svg">
    <defs>
      <radialGradient id="bg-glow" cx="50%" cy="55%" r="70%">
        <stop offset="0" stop-color="var(--green-bright)"/>
        <stop offset=".65" stop-color="var(--green-mid)"/>
        <stop offset="1" stop-color="var(--green-mint)"/>
      </radialGradient>
      <radialGradient id="sun" cx="50%" cy="10%" r="95%">
        <stop offset="0" stop-color="var(--gold-light)"/>
        <stop offset=".55" stop-color="var(--gold)"/>
        <stop offset="1" stop-color="var(--orange)"/>
      </radialGradient>
      <linearGradient id="grass" x1="0" y1="0" x2="0" y2="1">
        <stop offset="0" stop-color="#3fae2a" stop-opacity="0"/>
        <stop offset=".35" stop-color="#2f9a24"/>
        <stop offset="1" stop-color="#14601a"/>
      </linearGradient>
      <radialGradient id="foliage" cx="50%" cy="50%" r="50%">
        <stop offset="0" stop-color="#2d7a2a"/>
        <stop offset=".7" stop-color="#3f9a35" stop-opacity=".8"/>
        <stop offset="1" stop-color="#3f9a35" stop-opacity="0"/>
      </radialGradient>
    </defs>

    <rect class="label-bg" width="1040" height="700" fill="url(#bg-glow)"/>

    <g class="sun-badge">
      <circle cx="520" cy="-10" r="440" fill="var(--orange)"/>
      <circle cx="520" cy="-10" r="428" fill="var(--gold)"/>
      <circle cx="520" cy="-10" r="420" fill="var(--ring-green)"/>
      <circle cx="520" cy="-10" r="412" fill="var(--gold)"/>
      <circle cx="520" cy="-10" r="404" fill="url(#sun)"/>
    </g>

    <text class="headline" x="520" y="112" text-anchor="middle" font-size="92" textLength="540" lengthAdjust="spacingAndGlyphs">Multi Purpose</text>
    <text class="headline" x="520" y="255" text-anchor="middle" font-size="150" textLength="560" lengthAdjust="spacingAndGlyphs">OINTMENT</text>

    <ellipse class="botanical" role="img" aria-label="Tropical leaves and hibiscus flowers around the brand name" cx="510" cy="390" rx="210" ry="130" fill="url(#foliage)"/>

    <g class="brand">
      <circle cx="424" cy="389" r="14" fill="var(--red)"/>
      <text class="brand-name" x="450" y="400">Vira Lunos</text>
    </g>

    <rect class="grass" role="img" aria-label="Grass meadow" x="0" y="570" width="1040" height="130" fill="url(#grass)"/>

    <g class="use-icons">
      <path role="img" aria-label="Close-up of skin with a small cut" d="M258 560 a50 50 0 0 1 100 0 z" fill="#f1a493" stroke="#fff" stroke-width="3"/>
      <path role="img" aria-label="Knee joint anatomy" d="M468 560 a50 50 0 0 1 100 0 z" fill="#1c2347" stroke="#fff" stroke-width="3"/>
      <path role="img" aria-label="Shoulder muscle anatomy" d="M710 560 a50 50 0 0 1 100 0 z" fill="#e07a5f" stroke="#fff" stroke-width="3"/>
    </g>

    <text class="use-area" x="308" y="603" text-anchor="middle">SKIN</text>
    <circle cx="398" cy="588" r="6" fill="var(--white)"/>
    <text class="use-area" x="518" y="603" text-anchor="middle">JOINTS</text>
    <circle cx="630" cy="588" r="6" fill="var(--white)"/>
    <text class="use-area" x="770" y="603" text-anchor="middle">MUSCLES</text>

    <g class="net-contents">
      <path d="M390 700 v-40 q0-22 22-22 h236 q22 0 22 22 v40 z" fill="var(--pill)" stroke="#2f7a2a" stroke-width="2"/>
      <text class="size" x="530" y="678" text-anchor="middle">2.54 OZ.&#160;&#160;&#160;75 ML</text>
    </g>
  </svg>
</main>
</body>
</html>
```